Design of a Label for a Candy Company
Fizz Rocket
Design of a Label for a Candy Company - Food
Creative Brief
The size of the label will be 4"x4". This will be then folded in half (4"x2") and affixed on to the top of the bagged candy product The Front of the label: 1) Logo name: Fizz Rocket (see; logo) 2) with the Tag line: The flavor is KaBlaZing 3) Name of product (see; list below, we can fill in the different names once the ideal font is chosen) 4) Net Weight: (we can fill this in but you can use 80gm as an example) It should be colorful to catch the eye The back of the label: The background should reflect the front label's colors and would include the following text Ingredients: Corn Syrup, Sugar, Citrus Acid, Starch, natural and Artificial Flavors ALLERGY INFORMATION: MANUFACTURED IN A FACILITY THAT PROCESSES PRODUCTS CONTAINING TRACES OF MILK, EGG, WHEAT, PEANUTS, TREE NUTS AND SOY. PACKAGED BY: Fizz Rocket Confectionery, Ste-Verlaine. Trinidad WI Email: fizz.rocket@mailvoro.com Tel: (868)-541-3908 Product of Canada Bar Code, Printer request leave space for bar code. These would be some of the Products Candy Corn Teal Loops Blue Raspberry Gummi Lizardtail Printer request Adobe Illustrator File. CS3 format Please don't hesitate to ask questions, Thank You
q7tenjo q7tenjo
Project has been upgraded to Guaranteed We're looking for an eye catching label that will 'pop' and catch consumers' attention - Try using different fonts - incorporate a 'fun' background Colorful Thanks
Please see Creative Brief

```html
<!DOCTYPE html>
<html lang="en">
<head>
<meta charset="utf-8">
<title>Fizz Rocket – Candy Label</title>
<link rel="stylesheet" href="https://fonts.googleapis.com/css2?family=Chewy&family=Open+Sans:wght@400;700&display=swap">
<style>
  :root {
    --bg: #0d0d0d;
    --red: #d8141c;
    --red-deep: #a80d14;
    --red-light: #ee2a2a;
    --yellow: #ffd21f;
    --white: #ffffff;
    --ink: #2a2a2a;
  }
  * { box-sizing: border-box; margin: 0; padding: 0; }
  html, body { width: 1200px; height: 874px; overflow: hidden; }
  body {
    background: var(--bg);
    font-family: "Open Sans", Arial, sans-serif;
    display: flex; align-items: center; justify-content: center; gap: 60px;
  }
  .display { font-family: "Chewy", "Arial Black", sans-serif; font-weight: 400; }
  .label {
    position: relative; width: 540px; height: 270px;
    background: radial-gradient(ellipse at 45% 40%, var(--red-light), var(--red) 55%, var(--red-deep));
    border-radius: 6px; overflow: hidden; color: var(--white);
  }
  .hang-hole {
    position: absolute; top: 14px; left: 50%; width: 18px; height: 18px;
    margin-left: -9px; border-radius: 50%; background: var(--bg);
  }
  /* front */
  .brand-name {
    position: absolute; left: 40px; top: 44px;
    font-size: 58px; line-height: 1; color: var(--yellow); white-space: nowrap;
  }
  .tagline {
    position: absolute; left: 140px; top: 122px; width: 200px;
    font-size: 24px; line-height: 1.05; color: var(--white); text-align: center;
  }
  .tagline span { display: block; font-size: 30px; color: var(--yellow); }
  .net-weight {
    position: absolute; left: 26px; top: 168px; width: 100px; height: 70px;
    background: var(--yellow); border-radius: 8px; color: var(--red-deep);
    text-align: center; padding-top: 6px;
  }
  .net-weight strong { display: block; font-size: 32px; line-height: 1.1; }
  .net-weight small { font-size: 13px; font-weight: 700; }
  .product-name {
    position: absolute; right: 14px; top: 124px; width: 170px;
    font-size: 26px; line-height: 1.1; color: var(--yellow);
    text-align: center; transform: rotate(-6deg);
  }
  /* back */
  .info-tab {
    position: absolute; height: 22px; padding: 0 14px;
    background: var(--yellow); color: var(--ink);
    font-size: 13px; font-weight: 700; line-height: 22px; border-radius: 4px 4px 0 0;
  }
  .info-box {
    position: absolute; background: var(--white); color: var(--ink);
    font-size: 11px; line-height: 1.35; text-align: center; padding: 8px 10px;
    border-radius: 3px;
  }
  .ingredients-tab { left: 40px; top: 40px; }
  .ingredients-box { left: 30px; top: 62px; width: 200px; height: 62px; }
  .allergy-tab { left: 320px; top: 40px; }
  .allergy-box { left: 300px; top: 62px; width: 210px; height: 90px; font-size: 10px; text-transform: uppercase; }
  .packaged-tab { left: 30px; top: 140px; border-radius: 4px; }
  .packaged-text { position: absolute; left: 32px; top: 168px; font-size: 12px; line-height: 1.4; }
  .origin-box { left: 30px; top: 240px; width: 130px; padding: 3px 6px; font-size: 11px; font-weight: 700; }
  .back-brand {
    position: absolute; left: 236px; top: 166px; width: 60px;
    font-size: 20px; line-height: 1; color: var(--yellow); text-align: center;
  }
  .barcode-space {
    left: 320px; top: 172px; width: 170px; height: 44px;
    line-height: 28px; font-size: 12px;
  }
</style>
</head>
<body>
  <section class="label label-front" aria-label="Front of label">
    <div class="hang-hole"></div>
    <div class="brand-name display">Fizz Rocket</div>
    <div class="tagline display">The flavor is<span>KaBlaZing</span></div>
    <div class="net-weight"><strong class="display">120g</strong><small>Net Weight</small></div>
    <div class="product-name display">Gummi Lizardtail</div>
  </section>

  <section class="label label-back" aria-label="Back of label">
    <div class="hang-hole"></div>
    <div class="info-tab ingredients-tab">Ingredients</div>
    <div class="info-box ingredients-box">Corn Syrup, Sugar, Citrus Acid, Starch, Natural and Artificial Flavors</div>
    <div class="info-tab allergy-tab">Allergy Information</div>
    <div class="info-box allergy-box">Manufactured in a facility that processes products containing traces of milk, egg, wheat, peanuts, tree nuts and soy.</div>
    <div class="info-tab packaged-tab">Packaged By</div>
    <div class="packaged-text">
      Fizz Rocket Confectionery,<br>
      Ste-Verlaine, Trinidad WI<br>
      Email: fizz.rocket@mailvoro.com<br>
      Tel: (868)-541-3908
    </div>
    <div class="info-box origin-box">Product of Canada</div>
    <div class="back-brand display">Fizz Rocket</div>
    <div class="info-box barcode-space">Bar Code</div>
  </section>
</body>
</html>
```